Dredging Contractors, we run amphibious walking dredges cleaning up waterways, mines etc

We need an updated web design for our company based in Australia.
We have 20t "Walking" amphibious excavators that service mining companies and governments, cleaning up waterways and pond systems.
We would like to see designs that reflect our cutting edge marine / technology that appeals to our engineering / civil / mining clients. As well as providing benefits by cleaning up our marine waterways.
We have an existing web page at www.marshtrekworks.com.au

Target Market(s)

Mining companies, engineers, council civil engineers, developers, waterways engineers

Industry/Entity Type

It Company

Requirements
Must have
• Logo, contact details, Photos of equipment page (Gallery), quotation page, Contact page, list of capabilities page (Products and services),

```html
<!DOCTYPE html>
<html lang="en">
<head>
<meta charset="utf-8">
<title>Marshtrek Works — Amphibious Dredging</title>
<link href="https://fonts.googleapis.com/css2?family=Ubuntu:wght@400;500;700&display=swap" rel="stylesheet">
<style>
:root{
  --teal:#138d9a;
  --teal-dark:#0f6f79;
  --nav-top:#2bb0a6;
  --nav-bottom:#1e9b95;
  --btn:#49b6cc;
  --ink:#3b3b3b;
  --muted:#555;
  --rule:#d6d6d6;
  --panel:#f6f6f6;
  --footer:#474747;
  --bullet:#e0524a;
}
*{margin:0;padding:0;box-sizing:border-box}
html,body{width:900px;height:1200px;overflow:hidden;background:#fff}
body{position:relative;font-family:"Ubuntu",sans-serif;color:var(--ink)}
.abs{position:absolute}
.header{left:0;top:0;width:900px;height:100px;background:linear-gradient(#ffffff,#ececec)}
.brand{left:99px;top:22px;display:flex;align-items:center;gap:8px}
.brand-dot{width:58px;height:58px;border-radius:50%;background:var(--teal)}
.brand-name{font-size:27px;font-weight:700;line-height:25px;color:var(--teal-dark);letter-spacing:.5px}
.top-links{right:98px;top:10px;font-size:9px;color:#555}
.top-links span{margin:0 4px;color:#999}
.contact-line{right:98px;font-size:14.5px;color:#444;text-align:right}
.contact-line b{font-weight:500;color:var(--teal)}
.contact-line small{font-size:9.5px;font-weight:500;color:var(--teal)}
.nav{left:98px;top:107px;width:704px;height:44px;border-radius:4px;background:linear-gradient(var(--nav-top),var(--nav-bottom));}
.nav a{position:absolute;top:16px;font-size:11px;color:#fff;text-decoration:none;letter-spacing:.2px}
.slider{left:97px;top:160px;width:706px;height:293px;background:#fff;border:1px solid #ddd;box-shadow:0 12px 10px -10px rgba(0,0,0,.35)}
.slide{left:3px;top:3px;width:698px;height:285px;background:linear-gradient(180deg,#6aa6df 0%,#7e9a6a 45%,#3f6d4a 65%,#cbbb99 100%)}
.dots-tab{left:291px;top:263px;width:124px;height:22px;background:#4bb4d2;clip-path:polygon(8% 0,92% 0,100% 100%,0 100%)}
.dot{top:8px;width:10px;height:10px;border-radius:50%;background:#1f5d73}
.dot.active{background:#111}
.welcome-title{left:0;top:488px;width:900px;text-align:center;font-size:21px;color:var(--teal)}
.welcome-text{left:98px;top:527px;width:704px;text-align:center;font-size:10.4px;line-height:17.6px;color:var(--muted)}
.panel{left:0;top:598px;width:900px;height:276px;background:var(--panel);border-top:1.5px solid var(--teal)}
h2{position:absolute;font-weight:400;font-size:17.5px;color:var(--teal);line-height:21px}
.thumb{width:146px;height:86px;background:#fff;border:1px solid #ddd;padding:2px}
.thumb div{width:100%;height:100%}
.vrule{width:1px;background:var(--rule)}
.list{list-style:none;font-size:9.5px;color:var(--muted)}
.list li{position:absolute;white-space:nowrap;padding-left:19px}
.list li::before{content:"";position:absolute;left:0;top:1px;width:9px;height:9px;border-radius:50%;background:var(--bullet)}
.list li::after{content:"";position:absolute;left:2.5px;top:3.5px;width:2.5px;height:2.5px;border-top:1.3px solid #fff;border-right:1.3px solid #fff;transform:rotate(45deg)}
.btn{height:24px;background:var(--btn);color:#fff;font-size:11px;display:flex;align-items:center;justify-content:center;border-radius:1px}
.video{left:517px;top:926px;width:286px;height:145px;background:#fff;border:1px solid #ddd;padding:3px;box-shadow:0 12px 10px -10px rgba(0,0,0,.35)}
.video-still{width:100%;height:100%;background:linear-gradient(180deg,#bcc3cc 0%,#9aa6b5 45%,#4f6d93 60%,#30507a 100%)}
.play{left:639px;top:976px;width:42px;height:42px;border-radius:50%;background:rgba(255,255,255,.9)}
.footer{left:0;top:1114px;width:900px;height:86px;background:var(--footer);color:#ddd;font-size:8.5px}
.social{top:31px;width:23px;height:23px;border-radius:3px}
</style>
</head>
<body>

<header class="abs header">
  <div class="abs brand"><div class="brand-dot"></div><div class="brand-name">MARSHTREK<br>WORKS</div></div>
  <div class="abs top-links">Links<span>|</span>Newsletter<span>|</span>Site Map</div>
  <div class="abs contact-line" style="top:44px">Call Dredge : <b>1300 555 018</b></div>
  <div class="abs contact-line" style="top:68px">Email : <small>info@marshtrekworks.com.au</small></div>
</header>

<nav class="abs nav">
  <a style="left:17px">HOME</a>
  <a style="left:100px">ABOUT US</a>
  <a style="left:207px">PRODUCT/SERVICES</a>
  <a style="left:365px">PHOTO GALLERY</a>
  <a style="left:503px">QUOTATION</a>
  <a style="left:622px">CONTACT US</a>
</nav>

<section class="abs slider">
  <div class="abs slide" role="img" aria-label="Photo of a green amphibious walking dredge on supports beside a waterway with a worker in hi-vis"></div>
  <div class="abs dots-tab">
    <div class="abs dot active" style="left:27px"></div>
    <div class="abs dot" style="left:46px"></div>
    <div class="abs dot" style="left:65px"></div>
    <div class="abs dot" style="left:85px"></div>
  </div>
</section>

<h1 class="abs welcome-title" style="font-weight:400">Welcome to Our Company Site</h1>
<p class="abs welcome-text">Marshtrek Works has been working as waterways engineers since 1995. Our amphibious dredges are highly mobile and is easily transported by truck to anywhere in Australia. Our portable dewatering systems enable us to pump straight from the dregde and dry material down to 25 microns. We are able to dredge small ponds or marinas&nbsp; to mine sludge or industrial dewatering projects.</p>

<section class="abs panel">
  <h2 style="left:97px;top:22px">Photo Gallery</h2>
  <div class="abs thumb" style="left:97px;top:59px"><div role="img" aria-label="Dredge pontoon on a river" style="background:linear-gradient(#b9d3ea,#4f7fa8)"></div></div>
  <div class="abs thumb" style="left:257px;top:59px"><div role="img" aria-label="Dredge loaded on a truck" style="background:linear-gradient(#8aa67a,#6d7c5a)"></div></div>
  <div class="abs thumb" style="left:416px;top:59px"><div role="img" aria-label="Excavator working in a pond" style="background:linear-gradient(#5e8fbf,#3a5a78)"></div></div>
  <div class="abs thumb" style="left:97px;top:166px"><div role="img" aria-label="Excavator bucket close-up" style="background:linear-gradient(#8aa0b0,#4e6a85)"></div></div>
  <div class="abs thumb" style="left:257px;top:166px"><div role="img" aria-label="Dredge moored in a marina" style="background:linear-gradient(#4f7f6a,#2c4c5a)"></div></div>
  <div class="abs thumb" style="left:416px;top:166px"><div role="img" aria-label="Weed rake clearing a creek" style="background:linear-gradient(#7f8f6a,#485a48)"></div></div>

  <div class="abs vrule" style="left:593px;top:25px;height:227px"></div>

  <h2 style="left:618px;top:22px">Product/Services</h2>
  <ul class="list">
    <li style="left:619px;top:57px">Tailings Dams / Pump Inlets / Outlets</li>
    <li style="left:619px;top:83px">Rivers / Creeks / Ponds</li>
    <li style="left:619px;top:110px">Boat / Channel Passage</li>
    <li style="left:619px;top:136px">Aquatic Weed Management</li>
    <li style="left:619px;top:162px">Civil Engineering</li>
    <li style="left:619px;top:188px">Flood Control - Creek Clearing</li>
  </ul>
  <div class="abs btn" style="left:620px;top:228px;width:75px">Read More</div>
</section>

<h2 style="left:97px;top:889px">Ideal applications for our multipurpose<br>dredger:</h2>
<ul class="list">
  <li style="left:98px;top:944px">Suction and backhoe dredging in rivers, canals, harbours, lakes and coastal waters.</li>
  <li style="left:98px;top:965px">Where a versatile dredger is needed, which can both pump and excavate.</li>
  <li style="left:98px;top:986px">Where pile driving in water or on the shoreline is needed.</li>
  <li style="left:98px;top:1007px">Where vegetation disturbs conventional dredgers.</li>
  <li style="left:98px;top:1028px">Where vegetation needs to be removed.</li>
  <li style="left:98px;top:1049px">Environmental dredging.</li>
</ul>
<div class="abs btn" style="left:98px;top:1081px;width:75px">Read More</div>

<div class="abs vrule" style="left:489px;top:895px;height:205px"></div>

<h2 style="left:518px;top:890px">Dredging Video</h2>
<div class="abs video"><div class="video-still" role="img" aria-label="Video still of an animated dredge model with excavator arm reaching below the waterline"></div></div>
<div class="abs play">
  <svg width="42" height="42" viewBox="0 0 42 42"><polygon points="16,12 31,21 16,30" fill="#444"/></svg>
</div>
<div class="abs btn" style="left:727px;top:1081px;width:75px">View All</div>

<footer class="abs footer">
  <div class="abs" style="left:98px;top:29px;line-height:17.5px">Copyright © 2013 Jordan Ellery - Marshtrek Works.<br>All Right Reserved</div>
  <div class="abs" style="left:634px;top:38px;font-size:10px">Connect wuth us:</div>
  <div class="abs social" style="left:721px;background:#3b5c9e"></div>
  <div class="abs social" style="left:749px;background:#3bb2e4"></div>
  <div class="abs social" style="left:777px;background:#cc2d2d"></div>
</footer>

</body>
</html>
```